existing Business Card Re design

We are wanting to re design our cards to reflect our new logo , i have attache the current business cards and new logo
i will need a business card that reflects the following information on each card.

card 1:
Harold Dunsby, President
555-382-9164
info@kpqfoamcoat.com

card 2:
Colin Thresher, Outside Sales
Office: 555-382-9164
Cell: 555-617-2048
Sales@kpqfoamcoat.com

Card 3
Louis Varcoe, Branch Manager
Office: 555-382-9164
Cell: 555-493-7752
Louis@kpqfoamcoat.com

Card 4
I will need a Generic card with no name on it just business
555-382-9164
info@kpqfoamcoat.com

Target Market(s)

Homeowners and Contractors

Contact Information for Business Card

We are wanting to re design our cards to reflect our new logo , i have attache the current business cards and new logo. same info on current card

card 1:
Harold Dunsby, President
555-382-9164
info@kpqfoamcoat.com

card 2:
Office: 555-382-9164
Cell: 555-617-2048
Sales@kpqfoamcoat.com

Card 3
Office: 555-382-9164
Cell: 555-493-7752
Louis@kpqfoamcoat.com

Card 4
555-382-9164
info@kpqfoamcoat.com

Requirements
Must have
• same info as current cards with a added business
"sanitizing"

```html
<!DOCTYPE html>
<html lang="en">
<head>
<meta charset="utf-8">
<title>KPQ Foam Coat – Business Card</title>
<link href="https://fonts.googleapis.com/css2?family=Lato:wght@400;700;900&display=swap" rel="stylesheet">
<style>
  :root {
    --stage: #e9eaec;
    --card-white: #ffffff;
    --card-black: #0b0c0e;
    --brand-blue: #2a8fd6;
    --brand-deep: #0f3f86;
    --ink-dark: #16243a;
    --ink-grey: #7d7f84;
    --edge-blue: #1f6fd1;
    --text-light: #f2f4f7;
  }
  * { box-sizing: border-box; margin: 0; padding: 0; }
  html, body {
    width: 1200px; height: 913px; overflow: hidden;
    background: var(--stage);
    font-family: "Lato", Arial, sans-serif;
  }
  .stage {
    width: 1200px; height: 913px;
    display: flex; align-items: center; justify-content: center; gap: 40px;
  }
  .card {
    width: 560px; height: 320px;
    position: relative;
    display: flex; align-items: center;
    border-bottom: 4px solid var(--edge-blue);
    box-shadow: 0 10px 24px rgba(0,0,0,0.18);
  }
  .card--front { background: var(--card-white); }
  .card--back {
    background: linear-gradient(115deg, var(--card-black) 0%, #1b1d21 55%, #3a3d42 70%, var(--card-black) 100%);
  }
  .brand {
    width: 280px; display: flex; align-items: center; justify-content: center; gap: 10px;
  }
  .brand__dot { width: 26px; height: 26px; border-radius: 50%; background: var(--brand-blue); flex: none; }
  .brand__name { font-weight: 900; font-size: 27px; letter-spacing: -0.3px; white-space: nowrap; }
  .card--front .brand__name { color: var(--ink-dark); }
  .card--back .brand__name { color: var(--text-light); }
  .divider { width: 1px; height: 170px; background: var(--brand-blue); flex: none; }
  .details { padding-left: 26px; }
  .details__name { color: var(--brand-blue); font-weight: 900; font-size: 27px; line-height: 1.1; }
  .details__title { color: var(--ink-grey); font-size: 14px; margin: 2px 0 12px; }
  .details__address { color: var(--ink-grey); font-size: 14px; line-height: 1.35; margin-bottom: 8px; }
  .contact { list-style: none; }
  .contact li {
    display: flex; align-items: center; gap: 8px;
    color: var(--ink-grey); font-size: 14px; line-height: 1.45;
  }
  .contact svg { width: 13px; height: 13px; flex: none; }
  .contact .accent { color: var(--brand-blue); }
  .services { list-style: none; padding-left: 34px; }
  .services li {
    color: var(--text-light); font-size: 15px; letter-spacing: 1px; text-transform: uppercase;
    line-height: 1.75; display: flex; align-items: center; gap: 14px;
  }
  .services li::before {
    content: ""; width: 6px; height: 6px; border-radius: 50%; background: var(--brand-blue);
  }
</style>
</head>
<body>
<main class="stage">
  <section class="card card--front" aria-label="Business card front">
    <div class="brand">
      <span class="brand__dot"></span>
      <span class="brand__name">KPQ Foam Coat</span>
    </div>
    <div class="divider"></div>
    <div class="details">
      <h1 class="details__name">Harold Dunsby</h1>
      <p class="details__title">Precident &amp; CEO</p>
      <p class="details__address">2716 Harlow Ave.<br>Suite 8 Fenwick, TX 75381</p>
      <ul class="contact">
        <li>
          <svg viewBox="0 0 16 16" aria-hidden="true"><path fill="#2a8fd6" d="M3.5 1.5l2.5 0 1 3.5-1.7 1.2a9 9 0 0 0 4.5 4.5L11 9l3.5 1v2.5c0 .8-.7 1.5-1.5 1.5C7 14 2 9 2 3c0-.8.7-1.5 1.5-1.5z"/></svg>
          555-382-9164
        </li>
        <li>
          <svg viewBox="0 0 16 16" aria-hidden="true"><rect x="1" y="3" width="14" height="10" fill="#2a8fd6"/><path d="M1.5 3.5L8 9l6.5-5.5" fill="none" stroke="#fff" stroke-width="1.2"/></svg>
          info@kpqfoamcoat.com
        </li>
        <li>
          <svg viewBox="0 0 16 16" aria-hidden="true"><circle cx="8" cy="8" r="6.5" fill="none" stroke="#2a8fd6" stroke-width="1.3"/><ellipse cx="8" cy="8" rx="2.8" ry="6.5" fill="none" stroke="#2a8fd6" stroke-width="1"/><path d="M1.5 8h13M2.5 5h11M2.5 11h11" stroke="#2a8fd6" stroke-width="1"/></svg>
          <span>www.<span class="accent">kpqfoamcoat</span>.com</span>
        </li>
        <li>
          <svg viewBox="0 0 16 16" aria-hidden="true"><circle cx="8" cy="8" r="6.5" fill="none" stroke="#2a8fd6" stroke-width="1.3"/></svg>
          kpqfoamcoat
        </li>
      </ul>
    </div>
  </section>

  <section class="card card--back" aria-label="Business card back">
    <div class="brand">
      <span class="brand__dot"></span>
      <span class="brand__name">KPQ Foam Coat</span>
    </div>
    <div class="divider"></div>
    <ul class="services">
      <li>Spray Foam</li>
      <li>Fiberglass</li>
      <li>Insulation</li>
      <li>Roofing</li>
      <li>Sanitizing</li>
    </ul>
  </section>
</main>
</body>
</html>
```